The 5 stages of grief experience

I'm an artist and I'm launching my art debut and i need a whole set of thing. I have the logo and the colors and the list of what I need:
Sponsorship proposal (I have the info to be pasted once design is ready)
Flyer for my art. It's about the 5 stages of grief and its like you go into a maze to go through each art instillation that takes you over each feeling, there is a lot of feelings and symmetry in the art.
Denial
Anger
Depression
Bargaining
Acceptance

Target Market(s)

Visual Art society

Font styles to use
Sans Serif

Colors
fee4d6
f8ba93
000000
5c5c5c
fbfbfb

Requirements
Must have
• Symmetry
• Feeling
• Strong message
• Bold
• An artistic idea I like a lot is a black and white moon changes and it's 5 different moons starting from a crescent ending in a full moon all next to each other or on top of each other and the phases underneath in small geometric font
Nice to have
• Softness
Should not have
• Femininity

```html
<!DOCTYPE html>
<html lang="en">
<head>
<meta charset="utf-8">
<title>KORA Arts Event – Sponsorship</title>
<link rel="stylesheet" href="https://fonts.googleapis.com/css2?family=Noto+Sans:wght@300;400;700;800&display=swap">
<style>
  :root{
    --blush:#fee4d6;
    --peach:#f8ba93;
    --ink:#000000;
    --slate:#5c5c5c;
    --paper:#fbfbfb;
  }
  *{box-sizing:border-box;margin:0;padding:0}
  html,body{width:848px;height:1200px;overflow:hidden;background:var(--paper)}
  body{font-family:"Noto Sans",sans-serif;color:var(--ink)}
  .sheet{
    position:relative;width:848px;height:1200px;
    background:var(--blush);border:8px solid var(--ink);overflow:hidden;
  }
  .brand{position:absolute;left:63px;top:36px;width:170px;text-align:center}
  .brand-mark{display:block;width:150px;height:150px;margin:0 auto;border-radius:50%;background:var(--ink)}
  .brand-name{display:block;margin-top:14px;font-size:38px;font-weight:400;letter-spacing:6px;line-height:1}
  .masthead{position:absolute;left:230px;top:42px;width:600px;text-align:center}
  .event-title{font-size:55px;font-weight:800;line-height:1.05;letter-spacing:0.5px}
  .event-date{font-size:43px;font-weight:300;line-height:1.15}
  .event-venue{font-size:45px;font-weight:800;line-height:1.2}
  .tab{
    position:absolute;left:0;top:267px;width:280px;height:33px;
    background:var(--ink);color:var(--paper);border-radius:0 10px 10px 0;
    font-size:19px;font-weight:700;padding:3px 0 0 18px;
  }
  .intro{position:absolute;left:18px;top:308px;width:806px}
  .intro h2{font-size:21px;font-weight:400;line-height:1.2}
  .intro p{font-size:15.4px;line-height:20.5px;text-align:justify}
  .panel-shape{position:absolute;left:0;top:0}
  .fit{position:absolute;left:18px;top:540px;width:270px;color:var(--paper)}
  .fit h3{font-size:19px;font-weight:700;margin-bottom:12px}
  .fit p{font-size:15.4px;line-height:20.5px;text-align:justify;margin-bottom:10px}
  .fit p.left{text-align:left}
  .about-title{position:absolute;left:285px;top:504px;font-size:20px;font-weight:700;color:var(--paper)}
  .about{position:absolute;left:8px;top:545px;width:812px;color:var(--paper)}
  .about .curve{float:left;width:380px;height:330px;shape-outside:circle(226px at 140px 157px)}
  .about p{font-size:15.4px;line-height:20.5px;text-align:justify;margin-bottom:10px}
  .cta{
    position:absolute;left:80px;top:947px;width:673px;height:260px;
    background:var(--ink);color:var(--paper);border-radius:18px 18px 0 0;
    text-align:center;padding:20px 18px 0;
  }
  .cta h3{font-size:20px;font-weight:700;margin-bottom:8px}
  .cta p{font-size:15.4px;line-height:20.5px;margin-bottom:9px}
</style>
</head>
<body>
<main class="sheet">
  <div class="brand">
    <span class="brand-mark"></span>
    <span class="brand-name">KORA</span>
  </div>

  <header class="masthead">
    <h1 class="event-title">KORA Arts Event</h1>
    <p class="event-date">April 12.13.14</p>
    <p class="event-venue">Sahar Art Gallery</p>
  </header>

  <div class="tab">Experience the art ...</div>

  <section class="intro">
    <h2>Its a win-win</h2>
    <p>• Sponsoring KORA Arts Event provides you the unique opportunity to connect with the art community in Saudi Arabia, to build brand awareness and show your company’s support of an important cause: the arts!</p>
    <p>• This event reaches a certain key audience segment and provides a fun, entertaining and inspiring way for you to help us reach the audience, VIPs and volunteers. Feel good about supporting our local arts, heritage and cultural organisations as you enjoy an unforgettable evening.</p>
  </section>

  <svg class="panel-shape" width="832" height="1184" viewBox="0 0 832 1184" aria-hidden="true">
    <polygon points="222,490 832,490 832,904 214,904" fill="var(--slate)"/>
    <circle cx="140" cy="694" r="221" fill="var(--blush)"/>
    <circle cx="140" cy="694" r="207" fill="var(--slate)"/>
  </svg>

  <section class="fit">
    <h3>Find your fit</h3>
    <p>• Looking for the opportunity to become apart of one the most unique events of the year, to put your company name in front of hundreds of sophisticated attendees.</p>
    <p class="left">• Want to show your employees and investors a dedication to our community.</p>
    <p class="left">• Consider a sponsorship at KORA Arts Event</p>
  </section>

  <h3 class="about-title">About the event</h3>
  <section class="about">
    <div class="curve"></div>
    <p>• Being the top events of the year, art exhibitions and galleries are highly requested in Saudi. Hence, an event with two different types of artists decided to collaborate to host for the first time an interactive art event for the very first time in saudi. Artists Reem AlHarbi and Faisal AlOmari are the founders of the KORA Arts Event and aim to portray art in a unique view to saudis art audience.</p>
    <p>• Targeting all art enthusiasts, we allow them to enjoy the arts while being apart of it andget the chance to enjoy various art pieces that carry meaning about human emotionsand social experiences. Furthermore, people that attend KORA Arts Event will get theopportunity to enjoy the arts while enjoying good food, drinks, and mingle with Saudi’s finest art community</p>
  </section>

  <section class="cta">
    <h3>Interested?</h3>
    <p>KORA Arts Event is really excited to present art in a unique way. For the first time in Saudi you get to “experience the art” and be part of it.</p>
    <p>Kindly find attached the event’s Sponsorship form agreement with all the 5 categories to choose from in the same email sent to you.</p>
    <p>For any further inquiries, please feel free to contact us at +966512345678 anytime after 12 pm.</p>
    <p>Or email us on koraevent.sa@mailbox.com</p>
  </section>
</main>
</body>
</html>
```